Business Card for Brevikpartners

Need to design a business card with attached logo

Target Market(s)

I'm a financial/Investment adviser so card must be professional

Industry/Entity Type

Business

Font styles to use
Serif
Sans Serif

Requirements
Must have
• Would like in include the GOLD version of my logo if possible

Teodor Brevik
President

Address is
4278 Pemberly Ave
Larkfield, Ca. 94617

Phone
628-647-3920
Fax
707-413-7782

Email
teodor@brevikpartners.example

I also need the following tag line at the bottom of card:

Investment Advisor Representative of and Securities offered
through Harwick Capital Brokerage, LLC Member NTVQA, OLBR
and Registered Investment Advisor.

Nice to have
• Split color in order to incorporate GOLD LOGO
Should not have

```html
<!DOCTYPE html>
<html lang="en">
<head>
<meta charset="utf-8">
<title>Brevik Partners – Business Card</title>
<link rel="stylesheet" href="https://fonts.googleapis.com/css2?family=Josefin+Sans:wght@300;400;700&display=swap">
<style>
  :root {
    --backdrop-light: #f2f2f2;
    --backdrop-dark: #c9c9c9;
    --card-grey: #66666b;
    --card-light: #e4e5e8;
    --gold: #c9a84c;
    --ink: #2b2b2e;
    --icon: #8a8a8f;
    --back-text: #a9a9ad;
  }
  * { box-sizing: border-box; margin: 0; padding: 0; }
  html, body { width: 1200px; height: 787px; overflow: hidden; }
  body {
    background: radial-gradient(ellipse at 50% 40%, var(--backdrop-light) 0%, var(--backdrop-dark) 100%);
    font-family: "Josefin Sans", Arial, sans-serif;
    color: var(--ink);
  }
  .sheet {
    width: 1200px;
    height: 787px;
    display: flex;
    align-items: center;
    justify-content: center;
    gap: 50px;
  }
  .card {
    width: 525px;
    height: 300px;
    box-shadow: 0 10px 24px rgba(0,0,0,0.18);
    position: relative;
    overflow: hidden;
  }

  /* Front */
  .card--front { display: flex; }
  .front__brand {
    width: 52%;
    background: var(--card-grey);
    display: flex;
    align-items: center;
    justify-content: center;
  }
  .brand-mark {
    display: flex;
    align-items: center;
    gap: 10px;
  }
  .brand-mark__dot {
    width: 20px; height: 20px;
    border-radius: 50%;
    background: var(--gold);
    flex: none;
  }
  .brand-mark__name {
    font-weight: 400;
    font-size: 26px;
    letter-spacing: 1px;
    color: var(--gold);
    white-space: nowrap;
  }
  .front__details {
    width: 48%;
    background: var(--card-light);
    padding: 34px 18px 0 24px;
  }
  .person__name {
    font-weight: 300;
    font-size: 21px;
    letter-spacing: 0.5px;
  }
  .person__title {
    font-weight: 700;
    font-size: 13px;
    color: var(--gold);
    margin-top: 4px;
  }
  .address {
    font-style: normal;
    font-weight: 300;
    font-size: 13px;
    line-height: 19px;
    margin-top: 40px;
  }
  .contact { list-style: none; margin-top: 28px; }
  .contact__item {
    display: flex;
    align-items: center;
    gap: 8px;
    font-weight: 300;
    font-size: 13px;
    line-height: 23px;
    white-space: nowrap;
  }
  .contact__icon { width: 14px; height: 14px; fill: var(--icon); flex: none; }

  /* Back */
  .card--back {
    background: var(--card-grey);
    display: flex;
    align-items: center;
    justify-content: center;
  }
  .card--back .brand-mark__name { font-size: 30px; }
  .disclaimer {
    position: absolute;
    left: 40px; right: 40px; bottom: 22px;
    text-align: center;
    font-weight: 300;
    font-size: 9px;
    line-height: 13px;
    color: var(--back-text);
  }
</style>
</head>
<body>
<main class="sheet">

  <section class="card card--front" aria-label="Business card front">
    <div class="front__brand">
      <div class="brand-mark">
        <span class="brand-mark__dot"></span>
        <span class="brand-mark__name">Brevik Partners</span>
      </div>
    </div>
    <div class="front__details">
      <h1 class="person__name">Teodor Brevik</h1>
      <p class="person__title">President</p>
      <address class="address">4278 Pemberly Ave<br>Larkfield, Ca 94617</address>
      <ul class="contact">
        <li class="contact__item">
          <svg class="contact__icon" viewBox="0 0 16 16" aria-hidden="true"><path d="M4 1l2.5 3-1.5 2c.8 1.8 2.2 3.2 4 4l2-1.5 3 2.5-1.5 2.5C7 13.5 2.5 9 1.5 2.5z"/></svg>
          <span>628-647-3920</span>
        </li>
        <li class="contact__item">
          <svg class="contact__icon" viewBox="0 0 16 16" aria-hidden="true"><rect x="4" y="1" width="8" height="4"/><rect x="1" y="6" width="14" height="6" rx="1"/><rect x="4" y="10" width="8" height="5" fill="#e4e5e8" stroke="#8a8a8f"/></svg>
          <span>707-413-7782</span>
        </li>
        <li class="contact__item">
          <svg class="contact__icon" viewBox="0 0 16 16" aria-hidden="true"><path d="M1 3h14v10H1z" fill="none" stroke="#8a8a8f" stroke-width="1.3"/><path d="M1 3l7 6 7-6" fill="none" stroke="#8a8a8f" stroke-width="1.3"/></svg>
          <span>teodor@brevikpartners.example</span>
        </li>
      </ul>
    </div>
  </section>

  <section class="card card--back" aria-label="Business card back">
    <div class="brand-mark">
      <span class="brand-mark__dot"></span>
      <span class="brand-mark__name">Brevik Partners</span>
    </div>
    <p class="disclaimer">Investment Advisor Representative of and Securities offered through Harwick Capital Brokerage, LLC Member NTVQA, OLBR and Registered Investment Advisor.</p>
  </section>

</main>
</body>
</html>
```